EYE CATCHING SIGNAGE

Kelbro is a manufacturer of fasteners (screws) of all types and sizes - www.kelbro.ca

Requirement:
Design signage that can be applied to the entire surface of an exterior metal door on the outside facing side exposed to the elements. Design signage for a windowed entrance

Target Market(s)

Street View - General Public

Industry/Entity Type

Manufacturing

Requirements
Must have
• Design signage that makes it unmistakeable what it is we do. Eye catching - can be easily seen from the street.
Should not have
• Difficult to discern or read the company name and logo from the street

```html
<!DOCTYPE html>
<html lang="en">
<head>
<meta charset="utf-8">
<title>Kelbro Door Signage</title>
<link href="https://fonts.googleapis.com/css2?family=Poppins:wght@500;600;700;800&display=swap" rel="stylesheet">
<style>
  :root {
    --sky-light: #2bb9ea;
    --sky-deep: #0a8fd6;
    --ink: #0d0d0d;
    --white: #ffffff;
    --steel-light: #e9ecef;
    --steel-mid: #b9c0c7;
    --page: #ffffff;
  }
  html, body {
    margin: 0;
    width: 1200px;
    height: 1200px;
    overflow: hidden;
    background: var(--page);
  }
  .canvas {
    position: relative;
    width: 1200px;
    height: 1200px;
  }
  .door-sign {
    position: absolute;
    left: 343px;
    top: 30px;
    width: 465px;
    height: 1030px;
    transform: scale(1.107);
    transform-origin: top left;
    overflow: hidden;
    background: var(--white);
    font-family: "Poppins", sans-serif;
    box-shadow: 0 0 0 1px #e3e6e9;
  }
  .backdrop {
    position: absolute;
    inset: 0;
  }
  .product-photo {
    position: absolute;
    left: 0;
    top: 600px;
    width: 465px;
    height: 280px;
    background: linear-gradient(180deg, rgba(255,255,255,0) 0%, var(--steel-light) 35%, var(--steel-mid) 70%, rgba(255,255,255,0.2) 100%);
  }
  .brand {
    position: absolute;
    left: 40px;
    top: 118px;
    display: flex;
    align-items: center;
    gap: 12px;
    color: var(--white);
    font-weight: 800;
    font-size: 44px;
    letter-spacing: 1px;
    line-height: 1;
  }
  .brand-dot {
    width: 26px;
    height: 26px;
    border-radius: 50%;
    background: var(--white);
  }
  .headline {
    position: absolute;
    left: 30px;
    top: 232px;
    margin: 0;
    color: var(--ink);
    font-weight: 700;
    line-height: 1.05;
  }
  .headline span { display: block; }
  .headline .line-a { font-size: 29px; }
  .headline .line-b { font-size: 38px; margin-top: 6px; }
  .headline .line-c { font-size: 22px; margin-top: 8px; }
  .headline .line-d { font-size: 57px; color: var(--white); font-weight: 800; margin-top: 4px; letter-spacing: 0.5px; }
  .size-range {
    position: absolute;
    left: 31px;
    top: 445px;
    margin: 0;
    color: var(--ink);
    font-weight: 600;
    font-size: 14.5px;
    line-height: 1.4;
  }
  .standards-note {
    position: absolute;
    left: 0;
    width: 465px;
    top: 893px;
    margin: 0;
    text-align: center;
    color: var(--ink);
    font-weight: 600;
    font-size: 11.5px;
    line-height: 1.6;
    letter-spacing: 0.2px;
  }
</style>
</head>
<body>
<main class="canvas">
  <section class="door-sign">
    <div class="product-photo" role="img" aria-label="Photo of assorted zinc-plated self-drilling screws, hex bolts and a nut"></div>
    <svg class="backdrop" width="465" height="1030" viewBox="0 0 465 1030" aria-hidden="true">
      <defs>
        <linearGradient id="skyFill" x1="0" y1="0" x2="1" y2="1">
          <stop offset="0" stop-color="var(--sky-deep)"/>
          <stop offset="0.5" stop-color="var(--sky-light)"/>
          <stop offset="1" stop-color="var(--sky-deep)"/>
        </linearGradient>
      </defs>
      <path d="M0 0 H465 V520 C420 560 330 615 210 635 C120 645 50 615 0 585 Z" fill="url(#skyFill)"/>
      <path d="M465 448 C400 510 290 575 170 578 C110 580 70 565 45 548 C90 590 150 605 215 600 C320 590 410 530 465 480 Z" fill="var(--white)"/>
      <path d="M465 545 C400 585 320 615 230 620 C180 622 130 612 95 600 C150 630 210 638 270 632 C350 622 420 592 465 565 Z" fill="var(--white)"/>
    </svg>

    <div class="brand"><span class="brand-dot"></span>KELBRO</div>

    <h1 class="headline">
      <span class="line-a">WE MANUFACTURE</span>
      <span class="line-b">COLD-HEADED,</span>
      <span class="line-c">EXTERNALLY THREADED</span>
      <span class="line-d">FASTENERS</span>
    </h1>

    <p class="size-range">Ranging in diameter from #2 to<br>3/8", and in lengths up to 4 1/2".</p>

    <p class="standards-note">ALL OUR PRODUCTS ARE MANUFACTURED IN<br>ACCORDANCE WITH ALL NFSI STANDARDS.</p>
  </section>
</main>
</body>
</html>
```